BRCW Business Cards

Business Cards should contain:
Bright Ridgecrest Coating Works
Felix Darrow
M: 0417 865 093
E: brightRCW@fernpost.example
BRCW logo
TCG logo
Painting & Decorating
Licence # 719362K
slogan: Trust the finish of careful hands

Target Market(s)

all aspect of painting

Industry/Entity Type

Trade

Contact Information for Business Card

Felix Darrow
M: 0417 865 093
E: brightRCW@fernpost.example
BRCW logo
TCG logo
Painting & Decorating
Licence # 719362K

Font styles to use
Serif
Sans Serif

Requirements
Must have
• clear design with nice backround
• two sides
• smal TCG logo
Nice to have
• easy to read
Should not have
• mess
• black
• plastics form

```html
<!DOCTYPE html>
<html lang="en">
<head>
<meta charset="utf-8">
<title>BRCW Business Card</title>
<link rel="stylesheet" href="https://fonts.googleapis.com/css2?family=PT+Sans+Narrow:wght@700&family=Source+Sans+3:wght@400;600&family=Vollkorn:wght@500&display=swap">
<style>
  :root {
    --page: #e8e5e2;
    --card: #f8f6f4;
    --teal: #1f4d48;
    --ink: #2b2b2b;
    --rule: #d7b8ae;
    --badge: #d9dde8;
    --band-a: #2f8f5a;
    --band-b: #e0673a;
    --band-c: #2a9aa8;
  }
  * { margin: 0; padding: 0; box-sizing: border-box; }
  html, body {
    width: 1200px; height: 900px; overflow: hidden;
    background: var(--page);
  }
  .card {
    position: absolute; left: 160px; top: 177px;
    width: 880px; height: 546px;
    background: var(--card);
    box-shadow: 0 10px 30px rgba(0,0,0,0.12);
    overflow: hidden;
  }
  .slogan {
    position: absolute; left: 254px; width: 326px; top: 68px;
    text-align: center; white-space: nowrap;
    font-family: "PT Sans Narrow", sans-serif; font-weight: 700;
    font-size: 23px; color: var(--teal);
  }
  .partner-badge {
    position: absolute; left: 640px; top: 20px;
    width: 164px; height: 118px; border-radius: 6px;
    background: var(--badge);
  }
  .holder-name {
    position: absolute; left: 55px; top: 146px;
    font-family: "Source Sans 3", sans-serif; font-weight: 600;
    font-size: 34px; color: var(--teal); white-space: nowrap;
  }
  .licence {
    position: absolute; right: 59px; top: 152px;
    font-family: "Source Sans 3", sans-serif; font-weight: 400;
    font-size: 26px; color: var(--teal); white-space: nowrap;
  }
  .licence strong { font-weight: 600; }
  .brand {
    position: absolute; left: 214px; top: 207px; height: 216px;
    display: flex; align-items: center;
  }
  .brand-mark {
    width: 110px; height: 110px; border-radius: 50%;
    background: var(--teal);
  }
  .brand-divider {
    width: 2px; height: 216px; background: var(--teal);
    margin: 0 22px 0 25px;
  }
  .brand-name {
    font-family: "Vollkorn", serif; font-weight: 500;
    color: var(--teal); line-height: 1.1; white-space: nowrap;
  }
  .brand-initials { display: block; font-size: 78px; line-height: 1; margin-bottom: 10px; letter-spacing: 1px; }
  .brand-full { display: block; font-size: 33px; }
  .contact {
    position: absolute; left: 0; width: 880px; top: 443px; height: 32px;
    font-family: "Source Sans 3", sans-serif; font-weight: 400;
    font-size: 23px; color: var(--ink); line-height: 32px;
  }
  .contact-phone { position: absolute; right: 564px; top: 0; white-space: nowrap; }
  .contact-sep {
    position: absolute; left: 348px; top: 1px;
    width: 2px; height: 30px; background: var(--rule);
  }
  .contact-email { position: absolute; left: 378px; top: 0; white-space: nowrap; }
  .pattern-band {
    position: absolute; left: 0; right: 0; bottom: 0; height: 40px;
    background: linear-gradient(90deg, var(--band-a), var(--band-b) 25%, var(--band-c) 50%, var(--band-a) 75%, var(--band-b));
    opacity: 0.85;
  }
</style>
</head>
<body>
  <div class="card">
    <p class="slogan">Trust the finish of careful hands</p>
    <div class="partner-badge" role="img" aria-label="Partner association badge"></div>
    <p class="holder-name">Felix Darrow</p>
    <p class="licence"><strong>Licence:</strong> 719362K</p>
    <div class="brand">
      <div class="brand-mark"></div>
      <div class="brand-divider"></div>
      <p class="brand-name">
        <span class="brand-initials">BRCW</span>
        <span class="brand-full">Bright Ridgecrest</span>
        <span class="brand-full">Coating Works</span>
      </p>
    </div>
    <div class="contact">
      <span class="contact-phone">0417 865 093</span>
      <span class="contact-sep"></span>
      <span class="contact-email">brightRCW@fernpost.example</span>
    </div>
    <div class="pattern-band" role="img" aria-label="Colourful triangle pattern band"></div>
  </div>
</body>
</html>
```